New online business - used mobile phones - needs unique eye catching web design that sets it apart

The Handset Bazaar
We are a new business looking for a rapid response for our web site design. We don't want a normal website....... we need to be creative - most important PLEASE view the attached files uploaded 3 March to ensure you get us :)
.
The Handset Bazaar buys new and damaged mobile phones from the public. A simple process they complete to sell their mobile to us; we want our website to reflect this.
Our website needs to be modern, edgy and fun, not corporate and definitely not like any other mobile phone buying site in the world today!!
Our name was taken from a play on the share/stock market which we have tried to bring into the design ....... it hasn't worked with early designs submitted. Now taking a different approach. Refer to new attached files which should help you visualise our concept.

We like layout from Sketch Flock – rtlbenoviqs #7132809 design as this is very close to our layout vision.
The first page to tell the public what we do, how we do it, and then they click to accept the instant online quote. (page two they complete details about the mobiles model & condition they are selling, then page three complete their personal details).
Our background preference is dark, blackboard or dark with slight texture
a) We love white on black/dark background either typewriter font or look like hand drawn refer to attached files & heronandfig.com.au site to see. Would Label font work???

b) Where the light blue colour is on #7132809 this needs to be like chromavell colour classic green, fern green or bright green, not fluorescent lime green or an insipid green.

c) The banner says The Handset Bazaar is open........... for buying mobiles for cash $$$ (we need people to know we BUY used/damaged phones)

d) We love colour either solid colour or looks like it has been coloured in on our dark background. Open to white or pastel background versions refer to attached coffee file.
We like Chromavell Orange 021,Haute Red,Dazzling Blue, Cyan Blue, Beetroot Purple, Island Green.
e) How it works – underneath this title put Our deal …………. It’s easy as…………..quote, post, get paid!!!
Quote – first circle hand drawn icon showing mobile phone & $ sign. Underneath it says .....Obtain Quote for Model & Condition
Post – second circle hand drawn icon show parcel. Underneath it says Free Post
Paid – third circle hand drawn icon showing large $ sign. Underneath it says Payment in Two Days
Plans - is swapped for wording- Get Market Quote with a large button which says GO or CLICK HERE (they click on the button & it takes them to the next page)
f) FAQ
Allow for six FAQ’s we will forward correct content to you for final design layout.

g) About Us
Please allow about a paragraph of text here, we will forward correct content to you for final design layout.
h) Contact Us
At the bottom where normal website have ………. home, contact details, blog, etc, please only put Email us & Call us, then social media icons for QV, Work Nest and Chirpel

I) LOGO We don’t have one yet, just put The Handset Bazaar at the top & it needs to be large sized font ................we are new and we need to push our name
If you are not clear on our vision ..........please email me and I will reply very quickly.
Thank you for taking the time to read & understand & get us:)

Target Market(s)

20-45 years any body with a spare smart phone that is lying around and they can get cash for. Target market could be slightly older to 50 but focus of 20-40's

Industry/Entity Type

Business

Number of Pages Required

3 page

Font styles to use
Other font styles liked:
• handwritten font or typewriter font

Requirements
Must have
• Read only attached files dated 4 March, tech error with other files, being removed.
• 1 Layout design of Sketch Flock – rtlbenoviqs #7132809
• 2 Hand drawn icons - refer to files
• 3 White font needs to look like hand written refer to heronandfig.com.au or typewriter font - large size font
• 4 Main colours are Black or dark background, green with white text, preference is hand drawn font. The three circles for quote, post & pay with hand drawn icons can be any colour ...... Purple for quote, orange for post & green for paid
• 5 Big green button underneath 3 circles quote/post/pay - customers click on big button to get instant quote
Nice to have
• Coloured in hand drawings as per file
• Great Hand drawings coloured in
Should not have
• NO template designs so it look like you just put some text & a photo. Don't fill the page with mobile phones, one or two is ok, mobile phone pictures date so fast.
• Cartoons

```html
<!DOCTYPE html>
<html lang="en">
<head>
<meta charset="utf-8">
<title>The Handset Bazaar</title>
<link rel="stylesheet" href="https://fonts.googleapis.com/css2?family=Special+Elite&family=Courier+Prime:wght@400;700&family=Roboto:wght@400;700&display=swap">
<style>
:root{
  --green:#19b98a;
  --green-deep:#12936d;
  --ink:#111;
  --board:#1c1d1d;
  --board-mid:#333434;
  --chalk:#ffffff;
  --chalk-dim:#8d8d8d;
  --paper:#ffffff;
  --paper-soft:#f3f3f3;
  --text-grey:#8a8a8a;
  --type:"Special Elite", "Courier Prime", monospace;
  --mono:"Courier Prime", "Courier New", monospace;
  --body:"Roboto", Arial, sans-serif;
}
*{box-sizing:border-box;margin:0;padding:0}
html,body{width:1200px;height:2381px;overflow:hidden;background:var(--paper)}
.canvas{position:relative;width:1200px;height:2381px;overflow:hidden;font-family:var(--type);color:var(--chalk)}
.abs{position:absolute}

/* header */
.site-header{left:0;top:0;width:1200px;height:132px;background:radial-gradient(ellipse at 50% 40%,#3a3b3b 0%,#202121 70%,#161717 100%);display:flex;align-items:center;justify-content:center}
.brand{font-family:var(--mono);font-weight:700;font-size:52px;letter-spacing:1px;color:var(--chalk)}

/* hero */
.hero{left:0;top:132px;width:1200px;height:514px;overflow:hidden;background:linear-gradient(100deg,#1a2340 0%,#223a7a 25%,#1b2a55 45%,#0f2a24 70%,#0c4a2c 100%)}
.hero-glow{left:600px;top:0;width:600px;height:514px;background:radial-gradient(circle at 80% 70%,rgba(60,200,90,.55) 0%,rgba(20,90,50,.3) 40%,transparent 70%)}
.hero-handset{left:175px;top:22px;width:285px;height:460px;border-radius:42px;background:linear-gradient(160deg,#f2f2f2,#d9d9d9)}
.hero-screen{left:196px;top:82px;width:243px;height:340px;border-radius:4px;background:linear-gradient(180deg,#4c5a86 0%,#8a6c8e 55%,#3b3f55 100%)}
.hero-title{left:468px;top:120px;width:620px;font-size:50px;line-height:78px;letter-spacing:1px;text-transform:uppercase;text-shadow:2px 2px 4px rgba(0,0,0,.6);background:rgba(0,0,0,.25);padding:0 10px}

/* how it works */
.how{left:0;top:646px;width:1200px;height:589px;background:var(--board-mid)}
.how-kicker{left:0;top:40px;width:1200px;text-align:center;font-size:35px;color:var(--green);letter-spacing:1px}
.how-deal{left:216px;top:100px;font-size:40px;line-height:48px;white-space:nowrap}
.how-deal .second{display:block;padding-left:281px}
.step-badge{width:190px;height:190px;border-radius:50%;background:#262727}
.step-name{width:300px;text-align:center;font-family:var(--mono);font-weight:700;font-size:32px}
.step-note{width:300px;text-align:center;font-size:17px;line-height:19px;color:var(--chalk-dim)}

/* quote band */
.quote-band{left:0;top:1235px;width:1200px;height:155px;background:#000}
.quote-label{left:318px;top:52px;font-family:var(--mono);font-weight:700;font-size:44px;letter-spacing:1px;white-space:nowrap}
.go-button{left:787px;top:32px;width:98px;height:98px;border-radius:50%;background:var(--green);display:flex;align-items:center;justify-content:center;font-family:var(--mono);font-weight:700;font-size:40px;color:var(--chalk)}

/* faq */
.faq{left:0;top:1390px;width:1200px;height:599px;background:var(--paper);color:var(--ink)}
.faq-title{left:135px;top:58px;font-family:var(--mono);font-weight:700;font-size:35px}
.faq-num{left:158px;width:28px;height:28px;border-radius:50%;background:#2b2b2b;color:#fff;font-family:var(--body);font-size:13px;font-style:italic;display:flex;align-items:center;justify-content:center}
.faq-q{left:206px;font-family:var(--mono);font-size:22px;color:var(--green-deep)}
.faq-rule{left:206px;width:843px;height:3px;background:#555;border-radius:2px;opacity:.75}
.faq-a{left:206px;top:195px;width:816px;font-family:var(--body);font-size:12.5px;line-height:16px;color:var(--text-grey)}

/* about */
.about{left:0;top:1989px;width:1200px;height:273px;background:var(--paper-soft);color:var(--ink)}
.about-title{left:170px;top:30px;font-family:var(--mono);font-weight:700;font-size:35px}
.about-title .accent{color:var(--green)}
.about-copy{left:170px;top:83px;width:846px;font-family:var(--body);font-size:13.5px;line-height:19.5px;color:#222}
.read-more{left:170px;top:222px;font-family:var(--body);font-weight:700;font-size:11.5px;color:var(--green-deep)}

/* footer */
.site-footer{left:0;top:2262px;width:1200px;height:119px;background:radial-gradient(ellipse at 50% 50%,#2c2d2d 0%,#1a1b1b 80%)}
.foot-phone{left:192px;top:28px;font-family:var(--mono);font-size:27px;white-space:nowrap}
.foot-mail{left:452px;top:36px;font-family:var(--mono);font-size:18px;white-space:nowrap}
.social{top:34px;font-family:var(--mono);font-size:18px;color:var(--chalk);white-space:nowrap}
.copyright{left:155px;top:84px;font-family:var(--mono);font-size:10px;letter-spacing:1px}
</style>
</head>
<body>
<div class="canvas">

  <header class="site-header abs">
    <h1 class="brand">The Handset Bazaar</h1>
  </header>

  <section class="hero abs">
    <div class="hero-glow abs" role="img" aria-label="Blurred stock ticker display with green and blue lights"></div>
    <div class="hero-handset abs" role="img" aria-label="White smartphone shown at an angle"></div>
    <div class="hero-screen abs" aria-hidden="true"></div>
    <h2 class="hero-title abs">The Handset Bazaar<br>is open for buying<br>mobiles for cash</h2>
  </section>

  <section class="how abs">
    <h3 class="how-kicker abs">HOW IT WORKS</h3>
    <p class="how-deal abs">Our deal...... It's easy as......<span class="second">quote, post, get paid</span></p>

    <div class="step-badge abs" style="left:176px;top:227px" role="img" aria-label="Hand drawn phone with dollar coin"></div>
    <div class="step-badge abs" style="left:503px;top:227px" role="img" aria-label="Hand drawn gift parcel"></div>
    <div class="step-badge abs" style="left:832px;top:227px" role="img" aria-label="Hand drawn money bag with dollar sign"></div>

    <svg class="abs" style="left:370px;top:280px" width="510" height="70" viewBox="0 0 510 70" aria-hidden="true">
      <g fill="none" stroke="#fff" stroke-width="3" stroke-linecap="round">
        <path d="M5 50 Q60 0 118 38"/><path d="M104 38 L118 38 L114 24"/>
        <path d="M335 48 Q390 0 448 36"/><path d="M434 37 L448 36 L443 22"/>
      </g>
    </svg>

    <p class="step-name abs" style="left:121px;top:451px">Quote</p>
    <p class="step-note abs" style="left:121px;top:503px">Obtain quote model<br>&amp; condition</p>
    <p class="step-name abs" style="left:448px;top:451px">Post</p>
    <p class="step-note abs" style="left:448px;top:503px">Post it for free</p>
    <p class="step-name abs" style="left:777px;top:451px">Get paid</p>
    <p class="step-note abs" style="left:777px;top:503px">get your payment<br>within 2 days</p>
  </section>

  <section class="quote-band abs">
    <svg class="abs" style="left:0;top:-12px" width="1200" height="140" viewBox="0 0 1200 140" aria-hidden="true">
      <g fill="none" stroke="#444" stroke-width="3" stroke-linecap="round">
        <path d="M208 0 Q200 80 290 92"/><path d="M276 80 L292 92 L276 104"/>
        <path d="M1000 0 Q1005 80 918 92"/><path d="M932 80 L916 92 L932 104"/>
      </g>
    </svg>
    <p class="quote-label abs">Get Market Quote</p>
    <a class="go-button abs">GO</a>
  </section>

  <section class="faq abs">
    <h3 class="faq-title abs">Frequently Asked Questions</h3>

    <span class="faq-num abs" style="top:139px">1</span>
    <p class="faq-q abs" style="top:138px">Lorem ipsum dolor sit amet ?</p>
    <div class="faq-rule abs" style="top:172px"></div>
    <p class="faq-a abs">Lorem ipsum dolor sit amet, consectetuer adipiscing elit, sed diam nonummy nibh euismod tincidunt ut laoreet dolore magna aliquam erat volutpat. Ut wisi enim ad minim veniam, quis nostrud exerci tation ullamcorper suscipit lobortis nisl ut aliquip ex ea commodo consequat. Duis autem vel eum iriure dolor in hendrerit in vulputate velit esse molestie consequat, vel illum dolore eu feugiat nulla facilisis at vero eros et accumsan et iusto odio dignissim qui blandit praesent luptatum zzril delenit augue duis dolore te feugait nulla facilisi.</p>

    <span class="faq-num abs" style="top:326px">2</span>
    <p class="faq-q abs" style="top:325px">Lorem ipsum dolor sit amet ?</p>
    <div class="faq-rule abs" style="top:358px"></div>

    <span class="faq-num abs" style="top:386px">3</span>
    <p class="faq-q abs" style="top:385px">Lorem ipsum dolor sit amet ?</p>
    <div class="faq-rule abs" style="top:418px"></div>

    <span class="faq-num abs" style="top:447px">4</span>
    <p class="faq-q abs" style="top:446px">Lorem ipsum dolor sit amet ?</p>
    <div class="faq-rule abs" style="top:479px"></div>

    <span class="faq-num abs" style="top:508px">5</span>
    <p class="faq-q abs" style="top:507px">Lorem ipsum dolor sit amet ?</p>
    <div class="faq-rule abs" style="top:540px"></div>
  </section>

  <section class="about abs">
    <h3 class="about-title abs">About <span class="accent">The Handset Bazaar</span></h3>
    <p class="about-copy abs">Lorem ipsum dolor sit amet, consectetuer adipiscing elit, sed diam nonummy nibh euismod tincidunt ut laoreet dolore magna aliquam erat volutpat. Ut wisi enim ad minim veniam, quis nostrud exerci tation ullamcorper suscipit lobortis nisl ut aliquip ex ea commodo consequat. Duis autem vel eum iriure dolor in hendrerit in vulputate velit esse molestie consequat, vel illum dolore eu feugiat nulla facilisis at vero eros et accumsan et iusto odio dignissim qui blandit praesent luptatum zzril delenit augue duis dolore te feugait nulla facilisi.<br>Lorem ipsum dolor sit amet, consectetuer adipiscing elit, sed diam nonummy nibh euismod tincidunt ut laoreet dolore magna aliquam erat volutpat. Ut wisi enim ad minim veniam, quis nostrud exerci tation ullamcorper suscipit lobortis nisl ut aliquip ex ea commodo consequat.</p>
    <a class="read-more abs">READ MORE</a>
  </section>

  <footer class="site-footer abs">
    <svg class="abs" style="left:155px;top:24px" width="26" height="40" viewBox="0 0 26 40" aria-hidden="true">
      <rect x="3" y="2" width="20" height="36" rx="4" fill="none" stroke="#19b98a" stroke-width="3"/>
      <line x1="10" y1="32" x2="16" y2="32" stroke="#19b98a" stroke-width="3"/>
    </svg>
    <p class="foot-phone abs">555 018 2046</p>
    <svg class="abs" style="left:410px;top:38px" width="32" height="22" viewBox="0 0 32 22" aria-hidden="true">
      <rect x="2" y="2" width="28" height="18" fill="none" stroke="#19b98a" stroke-width="2.5"/>
      <path d="M2 2 L16 13 L30 2" fill="none" stroke="#19b98a" stroke-width="2.5"/>
    </svg>
    <p class="foot-mail abs">info@thehandsetbazaar.com</p>
    <span class="social abs" style="left:895px">QV</span>
    <span class="social abs" style="left:945px">Chirpel</span>
    <span class="social abs" style="left:1045px">Circlet</span>
    <p class="copyright abs">COPYRIGHT 2015 THE HANDSET BAZAAR. ALL RIGHTS RESERVED.</p>
  </footer>

</div>
</body>
</html>
```